Verdalunex webpage design

We are offering eco/sustainable theme vacations and make them bookable via our site. Our reference site is www.voyelmora.com. We want something similar but with a bit more creativity and elegant design. In our colors, which would depend on our logo colors.

NB: WE ARE NOT ASKING FOR A FULL BLOWN SITE. WE NEED 2 PAGE DESIGN FOR THE FIRST IMPRESSION. AFTER THAT WE CREATE A BUDGET FOR COMPLETION OF THE PROJECT.

Target Market(s)

Eco/Sustainable tourism.

Industry/Entity Type

Tourism

Coding

Coded - Design and coding required

Number of Pages Required

2 page

Requirements
Must have
• Reference site is voyelmora.com. But be creative and design something a bit different and more beautiful.
• NB: WE ARE NOT ASKING FOR A FULL BLOWN SITE. WE NEED 2 PAGE DESIGN FOR THE FIRST IMPRESSION. AFTER THAT WE CREATE A BUDGET FOR COMPLETION OF THE PROJECT.
• Please see our logo.

```html
<!DOCTYPE html>
<html lang="en">
<head>
<meta charset="utf-8">
<title>Verdalunex – Memorable Travel Experience</title>
<link href="https://fonts.googleapis.com/css2?family=Montserrat:wght@400;500;600;700;800&family=Open+Sans:wght@400;600;700&display=swap" rel="stylesheet">
<style>
:root{
  --mint:#74d6b8;
  --mint-soft:#a8e6d3;
  --teal:#1f8d78;
  --forest:#2d5b4f;
  --forest-deep:#234a40;
  --ink:#2f3437;
  --muted:#7b8288;
  --line:#e3e6e8;
  --page:#f4f5f7;
  --white:#ffffff;
  --star:#f4b400;
}
*{box-sizing:border-box;margin:0;padding:0}
html,body{width:1200px;height:5187px;overflow:hidden}
body{position:relative;background:var(--white);font-family:"Open Sans",Arial,sans-serif;color:var(--ink);font-size:14px}
.heading{font-family:"Montserrat",Arial,sans-serif}

/* hero */
.hero{position:absolute;left:0;top:0;width:1200px;height:780px;overflow:hidden}
.hero-photo{position:absolute;inset:0;background:
  radial-gradient(ellipse at 70% 25%,#c9a7b8 0%,rgba(201,167,184,0) 45%),
  linear-gradient(180deg,#6e6a8f 0%,#8d7aa0 25%,#6a5a78 48%,#4a3c4c 65%,#2f2a33 100%)}
.nav{position:absolute;top:48px;left:40px;right:40px;display:flex;align-items:center;justify-content:space-between}
.brand{font-family:"Montserrat",Arial,sans-serif;font-weight:500;font-size:40px;color:var(--white);display:flex;align-items:center;gap:10px;letter-spacing:.5px}
.brand-dot{width:14px;height:14px;border-radius:50%;background:var(--white)}
.nav-links{display:flex;align-items:center;gap:34px;color:var(--white);font-size:14px;font-weight:600}
.nav-links span{display:flex;align-items:center;gap:6px}
.btn-signup{background:var(--mint);padding:7px 14px;border-radius:3px}
.hero-title{position:absolute;top:245px;width:100%;text-align:center;color:var(--white);font-weight:700;font-size:50px;text-shadow:0 2px 8px rgba(0,0,0,.35)}
.hero-sub{position:absolute;top:318px;width:100%;text-align:center;color:var(--white);font-weight:600;font-size:20px}
.search{position:absolute;top:373px;left:121px;width:958px;height:83px;background:var(--white);border-radius:8px;display:flex;align-items:center;box-shadow:0 6px 20px rgba(0,0,0,.25)}
.search-field{flex:1;display:flex;align-items:center;gap:14px;padding-left:24px;height:54px;border-right:1px solid var(--line)}
.search-field:nth-child(3){border-right:none}
.search-label{font-size:11px;font-weight:700;text-transform:uppercase;color:var(--ink)}
.search-value{font-size:17px;color:var(--muted)}
.search-btn{width:72px;height:70px;margin-right:7px;border-radius:6px;background:var(--mint);display:flex;align-items:center;justify-content:center}
.stats{position:absolute;top:615px;left:0;width:100%;height:165px;background:rgba(34,34,40,.82);display:flex;justify-content:center;gap:110px;align-items:center}
.stat{display:flex;align-items:center;gap:18px;color:var(--white)}
.stat-num{font-family:"Montserrat",Arial,sans-serif;font-weight:800;font-size:44px;line-height:1}
.stat-label{color:var(--mint);font-weight:700;font-size:17px;margin-top:4px}

/* main */
.listing{position:absolute;top:847px;left:0;width:1200px;height:2350px;background:var(--page)}
.sidebar{position:absolute;left:62px;top:11px;width:374px}
.filter{background:var(--white);margin-bottom:36px;box-shadow:0 2px 8px rgba(0,0,0,.08)}
.filter-head{height:54px;background:var(--mint);color:var(--white);display:flex;align-items:center;gap:14px;padding-left:22px;font-family:"Montserrat",Arial,sans-serif;font-weight:700;font-size:18px}
.filter-body{padding:12px 22px 18px}
.select-row{height:50px;display:flex;align-items:center;justify-content:space-between;border-bottom:1px solid var(--line);font-size:14px}
.select-row::after{content:"";border-left:7px solid transparent;border-right:7px solid transparent;border-top:8px solid var(--ink)}
.radio{display:flex;align-items:center;gap:10px;height:30px;font-size:14px}
.radio::before{content:"";width:14px;height:14px;border:1.5px solid var(--muted);border-radius:50%}
.show-more{color:var(--teal);font-weight:600;font-size:13px;margin-top:4px}

.results{position:absolute;left:477px;top:11px;width:664px}
.sort{font-size:14px;margin-bottom:26px;height:25px}
.sort b{font-weight:600}
.card{background:var(--white);height:390px;margin-bottom:44px;box-shadow:0 2px 10px rgba(0,0,0,.08);position:relative;overflow:hidden}
.card-title{height:64px;background:#eeeff1;display:flex;align-items:center;justify-content:space-between;padding:0 22px;font-family:"Montserrat",Arial,sans-serif;font-weight:700;font-size:18px}
.card-body{display:flex;gap:34px;padding:28px 24px 0}
.card-photo{width:208px;height:160px}
.stars{display:flex;gap:3px;align-items:center;font-size:13px;color:var(--muted)}
.price-from{font-size:20px;margin-top:10px}
.price{font-family:"Montserrat",Arial,sans-serif;font-weight:700;font-size:34px;line-height:1.1}
.meta{display:flex;align-items:center;gap:12px;font-size:14px;margin-top:10px}
.card-foot{position:absolute;left:0;right:0;bottom:0;height:86px;border-top:1px solid var(--line);display:flex;align-items:center;padding-left:18px;gap:22px}
.feature{display:flex;align-items:center;gap:10px;font-size:14px;font-weight:600;line-height:1.15;width:150px}
.feature-icon{width:30px;height:30px;border:1.5px solid var(--muted);border-radius:50%;flex:none}
.see-details{position:absolute;right:0;bottom:0;width:170px;height:100px;background:var(--mint);clip-path:polygon(28% 0,100% 0,100% 100%,0 100%);color:var(--white);font-weight:700;font-size:17px;display:flex;align-items:center;justify-content:flex-end;padding-right:20px}
.load-more{position:absolute;left:606px;top:3070px;width:220px;height:56px;border-radius:4px;background:#c9ccd0;color:var(--white);font-weight:700;font-size:17px;display:flex;align-items:center;justify-content:center;gap:10px}

/* discover */
.discover{position:absolute;top:3197px;left:0;width:1200px;height:640px;background:var(--white)}
.discover h2{position:absolute;top:72px;width:100%;text-align:center;font-family:"Montserrat",Arial,sans-serif;font-weight:700;font-size:27px;line-height:1.45}
.discover h2 em{font-style:normal;color:var(--teal)}
.world{position:absolute;left:100px;top:172px;width:1000px;height:316px;background:radial-gradient(ellipse at 50% 55%,#eef0f1 0%,#ffffff 70%)}

/* reviews */
.reviews{position:absolute;top:3837px;left:0;width:1200px;height:420px;background:var(--page)}
.reviews h2{position:absolute;top:82px;width:100%;text-align:center;font-family:"Montserrat",Arial,sans-serif;font-weight:700;font-size:32px}
.reviews .rating{position:absolute;top:130px;width:100%;text-align:center;font-size:14px}
.arrow{position:absolute;top:282px;width:18px;height:18px;border-left:4px solid var(--ink);border-bottom:4px solid var(--ink)}
.review{position:absolute;top:200px;width:440px;display:flex;gap:26px}
.avatar{width:120px;height:120px;border-radius:50%;background:linear-gradient(160deg,#e6d5c8,#b79c88);flex:none}
.review-head{display:flex;gap:10px;align-items:center;font-size:13px;color:var(--muted)}
.review h3{font-size:19px;font-weight:700;margin:10px 0 6px}
.review p{font-size:13px;line-height:1.5;color:#555}
.review .author{margin-top:12px;font-size:13px;font-weight:700;color:var(--ink)}
.review .author span{display:block;font-weight:400}

/* newsletter */
.newsletter{position:absolute;top:4364px;left:0;width:1200px;height:297px;background:var(--forest)}
.news-badge{position:absolute;left:0;top:0;width:622px;height:297px;background:var(--mint);clip-path:polygon(0 0,88% 0,100% 50%,88% 100%,0 100%)}
.news-title{position:absolute;left:140px;top:108px;font-family:"Montserrat",Arial,sans-serif;font-weight:600;font-size:42px;color:var(--forest-deep);letter-spacing:3px}
.news-sub{position:absolute;left:150px;top:162px;font-family:"Montserrat",Arial,sans-serif;font-size:20px;letter-spacing:11px;color:var(--forest-deep)}
.news-copy{position:absolute;left:690px;top:80px;width:460px;color:var(--white);font-weight:700;font-size:20px;line-height:1.35}
.news-input{position:absolute;left:690px;top:175px;width:445px;height:58px;border-radius:29px;background:var(--forest-deep);border:1px solid #3d7062;display:flex;align-items:center;justify-content:space-between;padding:0 10px 0 24px;color:var(--white);font-weight:600;font-size:18px}
.news-go{width:40px;height:40px;border-radius:50%;background:var(--mint);display:flex;align-items:center;justify-content:center}

/* footer */
.footer{position:absolute;top:4661px;left:0;width:1200px;height:526px;background:var(--white)}
.footer-brand{position:absolute;top:130px;width:100%;text-align:center;font-family:"Montserrat",Arial,sans-serif;font-weight:500;font-size:50px;color:var(--ink)}
.footer-col{position:absolute;top:272px;font-size:13px;line-height:1.55}
.footer-col h4{color:var(--teal);font-size:13px;font-weight:700;text-transform:uppercase;margin-bottom:14px}
.contact-line{display:flex;gap:10px;margin-bottom:10px}
.contact-line i{width:14px;height:14px;border-radius:50%;border:1.5px solid var(--muted);flex:none;margin-top:2px}
.social-line{display:flex;align-items:center;gap:10px;margin-bottom:12px}
.social-line i{width:18px;height:18px;border-radius:3px;background:var(--ink);flex:none}
.copyright{position:absolute;bottom:0;left:0;width:100%;height:54px;border-top:1px solid var(--line);display:flex;align-items:center;justify-content:center;font-size:11px;color:var(--muted);letter-spacing:.5px}
</style>
</head>
<body>

<header class="hero">
  <div class="hero-photo" role="img" aria-label="Dusk photograph of a hillside coastal village above the sea"></div>
  <nav class="nav">
    <div class="brand"><span class="brand-dot"></span>Verdalunex</div>
    <div class="nav-links">
      <span>USD</span>
      <span><svg width="16" height="14" viewBox="0 0 16 14"><path d="M8 13 1.5 6.5A3.5 3.5 0 0 1 8 2.3 3.5 3.5 0 0 1 14.5 6.5Z" fill="none" stroke="#fff" stroke-width="1.6"/></svg>Favorites (0)</span>
      <span>Partners</span>
      <span><svg width="14" height="16" viewBox="0 0 14 16"><rect x="2" y="7" width="10" height="8" rx="1" fill="none" stroke="#fff" stroke-width="1.6"/><path d="M4 7V4.5a3 3 0 0 1 6 0V7" fill="none" stroke="#fff" stroke-width="1.6"/></svg>Log in</span>
      <span class="btn-signup">Sign Up</span>
    </div>
  </nav>
  <h1 class="hero-title heading">Memorable Travel Experience</h1>
  <p class="hero-sub">Unique holidays, organized by passionate experts</p>
  <form class="search">
    <div class="search-field">
      <svg width="22" height="28" viewBox="0 0 22 28"><path d="M11 27S2 16 2 10a9 9 0 0 1 18 0c0 6-9 17-9 17Z" fill="none" stroke="#1f8d78" stroke-width="2.2"/><circle cx="11" cy="10" r="3.5" fill="none" stroke="#1f8d78" stroke-width="2.2"/></svg>
      <div><div class="search-label">Destination</div><div class="search-value">Any Destination</div></div>
    </div>
    <div class="search-field">
      <svg width="26" height="26" viewBox="0 0 26 26"><rect x="2" y="4" width="22" height="20" rx="2" fill="none" stroke="#1f8d78" stroke-width="2.2"/><path d="M2 10h22M8 1v6M18 1v6" stroke="#1f8d78" stroke-width="2.2"/></svg>
      <div><div class="search-label">Duration and Arrival</div><div class="search-value">Select Date</div></div>
    </div>
    <div class="search-field">
      <svg width="28" height="28" viewBox="0 0 28 28"><path d="M14 2l3.6 7.6 8.2 1-6 5.7 1.6 8.2L14 20.5l-7.4 4 1.6-8.2-6-5.7 8.2-1Z" fill="none" stroke="#1f8d78" stroke-width="2"/></svg>
      <div><div class="search-label">Activity Type</div><div class="search-value">Any Category</div></div>
    </div>
    <div class="search-btn"><svg width="32" height="32" viewBox="0 0 32 32"><circle cx="13" cy="13" r="9.5" fill="none" stroke="#fff" stroke-width="3"/><path d="M20 20l9 9" stroke="#fff" stroke-width="3.4" stroke-linecap="round"/></svg></div>
  </form>
  <div class="stats">
    <div class="stat">
      <svg width="64" height="64" viewBox="0 0 64 64"><circle cx="32" cy="32" r="26" fill="none" stroke="#74d6b8" stroke-width="3"/><path d="M6 32h52M32 6c-10 10-10 42 0 52M32 6c10 10 10 42 0 52" fill="none" stroke="#74d6b8" stroke-width="2.5"/></svg>
      <div><div class="stat-num">300+</div><div class="stat-label">Verdalunexers</div></div>
    </div>
    <div class="stat">
      <svg width="64" height="64" viewBox="0 0 64 64"><rect x="8" y="18" width="44" height="28" rx="3" transform="rotate(-20 30 32)" fill="none" stroke="#74d6b8" stroke-width="3"/><path d="M22 26l16 12M20 34l10 8" stroke="#74d6b8" stroke-width="2.5"/></svg>
      <div><div class="stat-num">15,000+</div><div class="stat-label">Travel Packages</div></div>
    </div>
    <div class="stat">
      <svg width="70" height="56" viewBox="0 0 70 56"><circle cx="35" cy="16" r="9" fill="#74d6b8"/><circle cx="14" cy="22" r="7" fill="#74d6b8"/><circle cx="56" cy="22" r="7" fill="#74d6b8"/><path d="M20 50a15 15 0 0 1 30 0ZM2 50a12 12 0 0 1 22-6v6ZM68 50a12 12 0 0 0-22-6v6Z" fill="#74d6b8"/></svg>
      <div><div class="stat-num">500,000+</div><div class="stat-label">Customers per Month</div></div>
    </div>
  </div>
</header>

<main class="listing">
  <aside class="sidebar">
    <section class="filter">
      <div class="filter-head"><svg width="22" height="18" viewBox="0 0 22 18"><path d="M1 3l6-2 8 3 6-2v13l-6 2-8-3-6 2Z" fill="none" stroke="#fff" stroke-width="1.8"/></svg>Destinations</div>
      <div class="filter-body">
        <div class="select-row">Europe</div>
        <div class="select-row">Asia &amp; Oceania</div>
        <div class="select-row">Africa &amp; Middle East</div>
        <div class="select-row">The Americas &amp; Caribbean</div>
      </div>
    </section>
    <section class="filter">
      <div class="filter-head"><svg width="20" height="20" viewBox="0 0 20 20"><rect x="1" y="3" width="18" height="16" rx="2" fill="none" stroke="#fff" stroke-width="1.8"/><path d="M1 8h18M6 1v4M14 1v4" stroke="#fff" stroke-width="1.8"/></svg>Arrival Date</div>
      <div class="filter-body">
        <div class="radio">2019 May (10234)</div>
        <div class="radio">2019 June (11365)</div>
        <div class="radio">2019 July (10610)</div>
        <div class="radio">2019 August (10325)</div>
        <div class="radio">2019 September (10626)</div>
        <div class="show-more">show more</div>
      </div>
    </section>
    <section class="filter">
      <div class="filter-head"><svg width="20" height="20" viewBox="0 0 20 20"><circle cx="10" cy="10" r="8.5" fill="none" stroke="#fff" stroke-width="1.8"/><path d="M10 5v5l3 3" fill="none" stroke="#fff" stroke-width="1.8"/></svg>Duration</div>
      <div class="filter-body">
        <div class="radio">2 days (792)</div>
        <div class="radio">From 2 to 7 days (8599)</div>
        <div class="radio">From 1 to 2 weeks (7106)</div>
        <div class="radio">More than 2 weeks (1090)</div>
      </div>
    </section>
    <section class="filter">
      <div class="filter-head"><svg width="22" height="20" viewBox="0 0 22 20"><path d="M1 12l20-8-4 14-6-5-4 4v-6Z" fill="none" stroke="#fff" stroke-width="1.8"/></svg>Airport Transfer</div>
      <div class="filter-body">
        <div class="radio">Airport transfer included (5153)</div>
        <div class="radio">Airport transfer available (2793)</div>
      </div>
    </section>
    <section class="filter">
      <div class="filter-head"><svg width="20" height="20" viewBox="0 0 20 20"><path d="M2 2h8l8 8-8 8-8-8Z" fill="none" stroke="#fff" stroke-width="1.8"/><circle cx="6" cy="6" r="1.6" fill="#fff"/></svg>Categories</div>
      <div class="filter-body">
        <div class="select-row">Accomodation Type</div>
        <div class="select-row">Activity</div>
        <div class="select-row">Audience</div>
        <div class="select-row">Budget</div>
        <div class="select-row">Duration</div>
        <div class="select-row">Experience Level</div>
        <div class="select-row">Experience Type</div>
        <div class="select-row">Focus/Atmosphere</div>
        <div class="select-row">Food</div>
        <div class="select-row">Intensity Level</div>
        <div class="select-row">Location</div>
        <div class="select-row">Special Occasion</div>
        <div class="select-row">Time Periods</div>
      </div>
    </section>
    <section class="filter">
      <div class="filter-head"><svg width="22" height="18" viewBox="0 0 22 18"><rect x="1" y="1" width="20" height="16" rx="2" fill="none" stroke="#fff" stroke-width="1.8"/><circle cx="11" cy="9" r="3.5" fill="none" stroke="#fff" stroke-width="1.8"/></svg>Price per Trip</div>
      <div class="filter-body">
        <div class="radio">From US$0 to US$112 (299)</div>
        <div class="radio">From US$112 to US$337 (1448)</div>
        <div class="radio">From US$337 to US$1,011 (6598)</div>
        <div class="radio">More than US$1,011 (8397)</div>
      </div>
    </section>
  </aside>

  <section class="results">
    <div class="sort">Sort by : <b>Recommended</b> &#9662;</div>

    <article class="card">
      <div class="card-title">5 Days Italy by Train Tour in Rome, Florence, Venice<svg width="24" height="22" viewBox="0 0 24 22"><path d="M12 20 2.5 10.5A5 5 0 0 1 12 4 5 5 0 0 1 21.5 10.5Z" fill="none" stroke="#74d6b8" stroke-width="2"/></svg></div>
      <div class="card-body">
        <div class="card-photo" role="img" aria-label="Photo of the Colosseum in Rome under a blue sky" style="background:linear-gradient(180deg,#7fb2e0 0%,#a9c9e6 45%,#b08a62 60%,#7d6047 100%)"></div>
        <div>
          <div class="stars"><svg width="100" height="18" viewBox="0 0 100 18"><g fill="#f4b400"><path id="s" d="M9 1l2.4 5 5.5.7-4 3.8 1 5.4L9 13.3 4.1 16l1-5.4-4-3.8 5.5-.7Z"/><use href="#s" x="20"/><use href="#s" x="40"/><use href="#s" x="60"/><use href="#s" x="80"/></g></svg>(3)</div>
          <div class="price-from">from</div>
          <div class="price">US$1,145</div>
          <div class="meta"><svg width="18" height="20" viewBox="0 0 18 20"><circle cx="9" cy="5" r="4.5" fill="#1f8d78"/><path d="M0 20a9 9 0 0 1 18 0Z" fill="#1f8d78"/></svg>1 person</div>
          <div class="meta"><svg width="20" height="18" viewBox="0 0 20 18"><path d="M0 2h4M7 2h13M0 9h4M7 9h13M0 16h4M7 16h13" stroke="#1f8d78" stroke-width="2.6"/></svg>13 days / 12 nights</div>
        </div>
      </div>
      <div class="card-foot">
        <div class="feature"><span class="feature-icon"></span>Flexible cancellation policy</div>
        <div class="feature"><span class="feature-icon"></span>Airport transfer included</div>
        <div class="feature"><span class="feature-icon"></span>All meals included</div>
      </div>
      <div class="see-details">See Details</div>
    </article>

    <article class="card">
      <div class="card-title">8 Days Northern Spain Guided Tour in Province of León<svg width="24" height="22" viewBox="0 0 24 22"><path d="M12 20 2.5 10.5A5 5 0 0 1 12 4 5 5 0 0 1 21.5 10.5Z" fill="none" stroke="#74d6b8" stroke-width="2"/></svg></div>
      <div class="card-body">
        <div class="card-photo" role="img" aria-label="Photo of a Spanish city skyline at golden hour" style="background:linear-gradient(180deg,#e9b27a 0%,#d9935a 45%,#9c6a45 70%,#5e4536 100%)"></div>
        <div>
          <div class="stars"><svg width="100" height="18" viewBox="0 0 100 18"><g fill="#f4b400"><use href="#s"/><use href="#s" x="20"/><use href="#s" x="40"/><use href="#s" x="60"/><use href="#s" x="80"/></g></svg>(3)</div>
          <div class="price-from">from</div>
          <div class="price">US$1,145</div>
          <div class="meta"><svg width="18" height="20" viewBox="0 0 18 20"><circle cx="9" cy="5" r="4.5" fill="#1f8d78"/><path d="M0 20a9 9 0 0 1 18 0Z" fill="#1f8d78"/></svg>1 person</div>
          <div class="meta"><svg width="20" height="18" viewBox="0 0 20 18"><path d="M0 2h4M7 2h13M0 9h4M7 9h13M0 16h4M7 16h13" stroke="#1f8d78" stroke-width="2.6"/></svg>13 days / 12 nights</div>
        </div>
      </div>
      <div class="card-foot">
        <div class="feature"><span class="feature-icon"></span>Flexible cancellation policy</div>
        <div class="feature"><span class="feature-icon"></span>Airport transfer included</div>
        <div class="feature"><span class="feature-icon"></span>All meals included</div>
      </div>
      <div class="see-details">See Details</div>
    </article>

    <article class="card">
      <div class="card-title">4 Days Luxury Tour of Madrid, Burgos, and<br>La Rioja in Spain<svg width="24" height="22" viewBox="0 0 24 22"><path d="M12 20 2.5 10.5A5 5 0 0 1 12 4 5 5 0 0 1 21.5 10.5Z" fill="none" stroke="#74d6b8" stroke-width="2"/></svg></div>
      <div class="card-body">
        <div class="card-photo" role="img" aria-label="Photo of a hilltop village overlooking Spanish valleys" style="background:linear-gradient(180deg,#8cbbe6 0%,#b5d2ea 40%,#9a9a70 60%,#6d7a4e 100%)"></div>
        <div>
          <div class="stars"><svg width="100" height="18" viewBox="0 0 100 18"><g fill="#f4b400"><use href="#s"/><use href="#s" x="20"/><use href="#s" x="40"/><use href="#s" x="60"/><use href="#s" x="80"/></g></svg>(3)</div>
          <div class="price-from">from</div>
          <div class="price">US$1,145</div>
          <div class="meta"><svg width="18" height="20" viewBox="0 0 18 20"><circle cx="9" cy="5" r="4.5" fill="#1f8d78"/><path d="M0 20a9 9 0 0 1 18 0Z" fill="#1f8d78"/></svg>1 person</div>
          <div class="meta"><svg width="20" height="18" viewBox="0 0 20 18"><path d="M0 2h4M7 2h13M0 9h4M7 9h13M0 16h4M7 16h13" stroke="#1f8d78" stroke-width="2.6"/></svg>13 days / 12 nights</div>
        </div>
      </div>
      <div class="card-foot">
        <div class="feature"><span class="feature-icon"></span>Flexible cancellation policy</div>
        <div class="feature"><span class="feature-icon"></span>Airport transfer included</div>
        <div class="feature"><span class="feature-icon"></span>All meals included</div>
      </div>
      <div class="see-details">See Details</div>
    </article>

    <article class="card">
      <div class="card-title">10 Days Guided Sightseeing Tour of Vietnam<svg width="24" height="22" viewBox="0 0 24 22"><path d="M12 20 2.5 10.5A5 5 0 0 1 12 4 5 5 0 0 1 21.5 10.5Z" fill="none" stroke="#74d6b8" stroke-width="2"/></svg></div>
      <div class="card-body">
        <div class="card-photo" role="img" aria-label="Photo of a colourful lantern-lit street in Vietnam" style="background:linear-gradient(180deg,#8fb56a 0%,#d9c27a 40%,#c98a4e 65%,#6d5a3e 100%)"></div>
        <div>
          <div class="stars"><svg width="100" height="18" viewBox="0 0 100 18"><g fill="#f4b400"><use href="#s"/><use href="#s" x="20"/><use href="#s" x="40"/><use href="#s" x="60"/><use href="#s" x="80"/></g></svg>(3)</div>
          <div class="price-from">from</div>
          <div class="price">US$1,145</div>
          <div class="meta"><svg width="18" height="20" viewBox="0 0 18 20"><circle cx="9" cy="5" r="4.5" fill="#1f8d78"/><path d="M0 20a9 9 0 0 1 18 0Z" fill="#1f8d78"/></svg>1 person</div>
          <div class="meta"><svg width="20" height="18" viewBox="0 0 20 18"><path d="M0 2h4M7 2h13M0 9h4M7 9h13M0 16h4M7 16h13" stroke="#1f8d78" stroke-width="2.6"/></svg>13 days / 12 nights</div>
        </div>
      </div>
      <div class="card-foot">
        <div class="feature"><span class="feature-icon"></span>Flexible cancellation policy</div>
        <div class="feature"><span class="feature-icon"></span>Airport transfer included</div>
        <div class="feature"><span class="feature-icon"></span>All meals included</div>
      </div>
      <div class="see-details">See Details</div>
    </article>

    <article class="card">
      <div class="card-title">8 Days Japan<svg width="24" height="22" viewBox="0 0 24 22"><path d="M12 20 2.5 10.5A5 5 0 0 1 12 4 5 5 0 0 1 21.5 10.5Z" fill="none" stroke="#74d6b8" stroke-width="2"/></svg></div>
      <div class="card-body">
        <div class="card-photo" role="img" aria-label="Photo of a Japanese pagoda with cherry blossoms" style="background:linear-gradient(180deg,#b9d4ec 0%,#e8cbd6 45%,#d7a7b8 65%,#7a6a6a 100%)"></div>
        <div>
          <div class="stars"><svg width="100" height="18" viewBox="0 0 100 18"><g fill="#f4b400"><use href="#s"/><use href="#s" x="20"/><use href="#s" x="40"/><use href="#s" x="60"/><use href="#s" x="80"/></g></svg>(3)</div>
          <div class="price-from">from</div>
          <div class="price">US$1,145</div>
          <div class="meta"><svg width="18" height="20" viewBox="0 0 18 20"><circle cx="9" cy="5" r="4.5" fill="#1f8d78"/><path d="M0 20a9 9 0 0 1 18 0Z" fill="#1f8d78"/></svg>1 person</div>
          <div class="meta"><svg width="20" height="18" viewBox="0 0 20 18"><path d="M0 2h4M7 2h13M0 9h4M7 9h13M0 16h4M7 16h13" stroke="#1f8d78" stroke-width="2.6"/></svg>13 days / 12 nights</div>
        </div>
      </div>
      <div class="card-foot">
        <div class="feature"><span class="feature-icon"></span>Flexible cancellation policy</div>
        <div class="feature"><span class="feature-icon"></span>Airport transfer included</div>
        <div class="feature"><span class="feature-icon"></span>All meals included</div>
      </div>
      <div class="see-details">See Details</div>
    </article>
  </section>
</main>

<div class="load-more"><svg width="20" height="20" viewBox="0 0 20 20"><circle cx="10" cy="10" r="8.5" fill="none" stroke="#fff" stroke-width="2"/><path d="M10 6v8M6 10l4 4 4-4" fill="none" stroke="#fff" stroke-width="2"/></svg>Load More</div>

<section class="discover">
  <h2>We enable you to easily <em>discover, plan, and book</em> unique<br>travel experiences anywhere in the world</h2>
  <div class="world" role="img" aria-label="Outline world map with circular travel photos pinned over different continents"></div>
</section>

<section class="reviews">
  <h2>Reviews from RevuSphere</h2>
  <p class="rating">Rated 8.7 out of 10 (Great) in 424 reviews</p>
  <span class="arrow" style="left:72px;transform:rotate(45deg)"></span>
  <span class="arrow" style="left:1110px;transform:rotate(-135deg)"></span>
  <article class="review" style="left:130px">
    <div class="avatar" role="img" aria-label="Reviewer portrait photo"></div>
    <div>
      <div class="review-head"><svg width="80" height="14" viewBox="0 0 100 18"><g fill="#1f8d78"><use href="#s"/><use href="#s" x="20"/><use href="#s" x="40"/><use href="#s" x="60"/><use href="#s" x="80"/></g></svg>Reviewed 2 days ago</div>
      <h3>Well Organized!</h3>
      <p>Our guide knew every trail and village, meals were local and fresh, and each transfer ran on time. A calm, thoughtful trip that felt kind to the places we visited. Highly recommended to friends.</p>
      <div class="author">Anna Morvell<span>Ancaster, ON</span></div>
    </div>
  </article>
  <article class="review" style="left:630px">
    <div class="avatar" role="img" aria-label="Reviewer portrait photo"></div>
    <div>
      <div class="review-head"><svg width="80" height="14" viewBox="0 0 100 18"><g fill="#1f8d78"><use href="#s"/><use href="#s" x="20"/><use href="#s" x="40"/><use href="#s" x="60"/><use href="#s" x="80"/></g></svg>Reviewed 2 days ago</div>
      <h3>Well Organized!</h3>
      <p>Booking was simple and the team answered every question quickly. The eco lodges were lovely, the pace relaxed, and we met wonderful hosts along the way. We are already planning our next holiday.</p>
      <div class="author">Janelle Carrow<span>Ancaster, ON</span></div>
    </div>
  </article>
</section>

<section class="newsletter">
  <div class="news-badge"></div>
  <div class="news-title">NEWSLETTER</div>
  <div class="news-sub">SUBSCRIPTION</div>
  <p class="news-copy">Register your email address to get more information about us and our promotion</p>
  <div class="news-input">Enter Your Email Address<span class="news-go"><svg width="18" height="16" viewBox="0 0 18 16"><path d="M1 8h14M10 2l6 6-6 6" fill="none" stroke="#234a40" stroke-width="2.4"/></svg></span></div>
</section>

<footer class="footer">
  <div class="footer-brand">Verdalunex</div>
  <div class="footer-col" style="left:121px">
    <h4>Quick Links</h4>
    About Verdalunex<br>Add/Manage Your Business<br>Become an Affiliate<br>Site Map<br>Work With Us
  </div>
  <div class="footer-col" style="left:408px">
    <h4>Recent Blog</h4>
    Berlin &amp; Christmas Traditions<br>The Best Ski &amp; Snowboard Festivals<br>Europe's Best Christmas Markets<br>A Hipster's Guide to London<br>A Guide to Authentic Mexican Food
  </div>
  <div class="footer-col" style="left:709px">
    <h4>Contact</h4>
    <div class="contact-line"><i></i><span>Verdalunex<br>42 Verbeekstraat<br>Utrecht, Netherland</span></div>
    <div class="contact-line"><i></i><span>0000 123 4567</span></div>
    <div class="contact-line"><i></i><span>info@verdalunex.com</span></div>
  </div>
  <div class="footer-col" style="left:1003px">
    <h4>Follow Us</h4>
    <div class="social-line"><i></i>Friendloop</div>
    <div class="social-line"><i></i>Chirpline</div>
    <div class="social-line"><i></i>Snapgrid</div>
  </div>
  <div class="copyright">COPYRIGHT © 2019 VERDALUNEX. ALL RIGHTS RESERVED.</div>
</footer>

</body>
</html>
```